Business card design needed

I need to display a copy of one of my paintings on front,
with my contact details displayed effectively within the painting.
On the back, my Logo needs to be displayed.
Font used should be artistic, but legible.
A high quality GLOSS Paper

Target Market(s)

Business people who purchase my Art for their premises and Boardrooms but also home owners both Traditional and Modern enthusiasts.

Industry/Entity Type

Business

Contact Information for Business Card

Artist /Interior Designer- Mellie Vantorski
Specializing in Oils on Canvas
Co-ordinate Colours in Home or Office
Over 25 years experience
mobile: 0492 581064
email: rowena.k@palvix.net.au
P.O. Box 518
Marlow Reach 2947 NSW

Requirements
Must have
• Good visual of painting, well proportioned.
Your can play with the description of Artist as long as it appeals to the above clientele.
Choose a painting which allows the potential client to see the text but showcases

the canvas too.

```html
<!DOCTYPE html>
<html lang="en">
<head>
<meta charset="utf-8">
<title>Mel Vantorski Art – Business Card</title>
<link rel="stylesheet" href="https://fonts.googleapis.com/css2?family=Cinzel:wght@400;600&family=Cinzel+Decorative:wght@700&family=Open+Sans:wght@400;700&display=swap">
<style>
  :root {
    --stage: #2b2b2b;
    --back-dark: #1e1c10;
    --back-mid: #3d3a1c;
    --gold: #f0cf3a;
    --tagline: #e9e4cf;
    --front-base: #2c2840;
    --front-deep: #221f33;
    --name-yellow: #f6e51a;
    --text-light: #ece9f4;
    --text-soft: #c9c4da;
    --paint-violet: #5a5a9a;
    --paint-blue: #6f86c8;
    --paint-green: #7a9a4a;
    --paint-grey: #8d8aa6;
  }
  * { box-sizing: border-box; margin: 0; padding: 0; }
  html, body {
    width: 1200px;
    height: 900px;
    overflow: hidden;
    background: var(--stage);
  }
  .canvas {
    width: 1200px;
    height: 900px;
    display: flex;
    flex-direction: column;
    align-items: center;
    justify-content: center;
    gap: 40px;
  }
  .card {
    position: relative;
    width: 640px;
    height: 360px;
    overflow: hidden;
    border-radius: 3px;
    box-shadow: 0 10px 30px rgba(0,0,0,.45);
  }

  /* Back of card: logo side */
  .card-back {
    background:
      radial-gradient(ellipse at 35% 55%, rgba(90,84,40,.55), transparent 60%),
      radial-gradient(ellipse at 75% 30%, rgba(70,64,30,.5), transparent 55%),
      linear-gradient(135deg, var(--back-mid), var(--back-dark));
  }
  .brand {
    position: absolute;
    left: 0; right: 0; top: 140px;
    text-align: center;
  }
  .brand-name {
    display: inline-flex;
    align-items: center;
    gap: 12px;
    font-family: "Cinzel", serif;
    font-weight: 600;
    font-size: 34px;
    letter-spacing: 2px;
    color: var(--gold);
  }
  .brand-dot {
    width: 10px; height: 10px;
    border-radius: 50%;
    background: var(--gold);
  }
  .brand-tagline {
    margin-top: 8px;
    font-family: "Cinzel", serif;
    font-weight: 400;
    font-size: 17px;
    letter-spacing: 1.5px;
    color: var(--tagline);
  }

  /* Front of card: painting with details */
  .card-front {
    background: linear-gradient(180deg, var(--front-base) 0%, var(--front-deep) 100%);
  }
  .painting {
    position: absolute;
    left: 0; top: 0;
    width: 100%;
    height: 230px;
    background:
      radial-gradient(ellipse at 20% 40%, var(--paint-blue), transparent 45%),
      radial-gradient(ellipse at 60% 30%, var(--paint-violet), transparent 50%),
      radial-gradient(ellipse at 85% 15%, var(--paint-green), transparent 35%),
      radial-gradient(ellipse at 40% 10%, var(--paint-grey), transparent 45%),
      linear-gradient(180deg, #4a4870 0%, #3a3658 70%, var(--front-base) 100%);
    -webkit-mask-image: linear-gradient(180deg, #000 70%, transparent 100%);
            mask-image: linear-gradient(180deg, #000 70%, transparent 100%);
  }
  .details {
    position: absolute;
    left: 36px; top: 228px;
    width: 300px;
  }
  .person-name {
    font-family: "Cinzel Decorative", serif;
    font-weight: 700;
    font-size: 27px;
    color: var(--name-yellow);
    line-height: 1.1;
  }
  .person-role {
    margin-top: 4px;
    font-family: "Open Sans", sans-serif;
    font-weight: 700;
    font-size: 13px;
    color: var(--text-light);
  }
  .person-summary {
    margin-top: 10px;
    font-family: "Open Sans", sans-serif;
    font-size: 12px;
    line-height: 1.45;
    color: var(--text-soft);
  }
  .contact {
    position: absolute;
    left: 380px; top: 226px;
    font-family: "Open Sans", sans-serif;
    font-size: 13px;
    line-height: 1.55;
    color: var(--text-light);
  }
  .contact-label {
    color: var(--name-yellow);
    font-weight: 400;
    font-size: 12px;
  }
  .contact-value { font-weight: 700; }
</style>
</head>
<body>
<main class="canvas">

  <section class="card card-back" aria-label="Card back">
    <div class="brand">
      <div class="brand-name"><span>Mel Vantorski Art</span><span class="brand-dot" aria-hidden="true"></span></div>
      <div class="brand-tagline">Original Paintings for Home &amp; Office</div>
    </div>
  </section>

  <section class="card card-front" aria-label="Card front">
    <div class="painting" role="img" aria-label="Oil painting of purple and blue wisteria blossoms with green leaves hanging from a grey branch"></div>

    <div class="details">
      <h1 class="person-name">Mellie Vantorski</h1>
      <p class="person-role">Artist /Interior Designer</p>
      <p class="person-summary">Specializing in Oils on Canvas Co-ordinate Colours in Home or Office Over 25 years experience.</p>
    </div>

    <div class="contact">
      <div><span class="contact-label">mobile:</span> <span class="contact-value">0492 581064</span></div>
      <div><span class="contact-label">email:</span> <span class="contact-value">rowena.k@palvix.net.au</span></div>
      <div class="contact-value">P.O. Box 518 Marlow Reach 2947 NSW</div>
    </div>
  </section>

</main>
</body>
</html>
```